Postcard Design

We have a church youth camp named Pell Ridge Camp and Retreat Lodge. Once a year we ask our clergy and parishioners to come to our camp to take part in what we call "Mend Days." 2015 will be Mend Days 3 and I would like to create a card that can be handed out as a reminder.

Industry/Entity Type

Church

```html
<!DOCTYPE html>
<html lang="en">
<head>
<meta charset="utf-8">
<title>Mend Days 2015 – Pell Ridge Camp</title>
<link href="https://fonts.googleapis.com/css2?family=Oswald:wght@300;400;500&family=Allura&family=Roboto+Condensed:ital,wght@0,500;1,300&display=swap" rel="stylesheet">
<style>
  :root {
    --ink: #1b1410;
    --sky-light: #fbd6a0;
    --sky-mid: #f0913f;
    --sky-deep: #c93c1f;
    --sky-dark: #7e1a12;
    --silhouette: #120c0a;
    --accent: #f3a846;
  }
  html, body {
    margin: 0;
    width: 1200px;
    height: 902px;
    overflow: hidden;
    background: #ffffff;
  }
  .postcard {
    position: relative;
    width: 1200px;
    height: 902px;
    overflow: hidden;
    color: var(--ink);
  }
  .sunset-sky {
    position: absolute;
    inset: 0;
    background:
      radial-gradient(ellipse 45% 40% at 32% 30%, var(--sky-light) 0%, rgba(251,214,160,0) 100%),
      radial-gradient(ellipse 70% 60% at 40% 45%, var(--sky-mid) 0%, rgba(240,145,63,0) 100%),
      linear-gradient(160deg, #f4a35c 0%, var(--sky-mid) 35%, var(--sky-deep) 70%, var(--sky-dark) 100%);
  }
  .cross-on-hill {
    position: absolute;
    right: 0;
    bottom: 0;
    width: 620px;
    height: 640px;
    background: radial-gradient(ellipse 90% 85% at 100% 100%, var(--silhouette) 0%, var(--silhouette) 40%, rgba(18,12,10,0.55) 65%, rgba(18,12,10,0) 100%);
  }
  .host {
    position: absolute;
    left: 72px;
    top: 104px;
    width: 740px;
    text-align: center;
    font-family: "Oswald", sans-serif;
    font-weight: 300;
    font-size: 40px;
    letter-spacing: 0.2px;
    margin: 0;
  }
  .presents {
    position: absolute;
    left: 72px;
    top: 178px;
    width: 740px;
    text-align: center;
    font-family: "Roboto Condensed", sans-serif;
    font-style: italic;
    font-weight: 300;
    font-size: 32px;
    margin: 0;
  }
  .event-title {
    position: absolute;
    left: 62px;
    top: 222px;
    width: 760px;
    text-align: center;
    font-family: "Allura", cursive;
    font-weight: 400;
    font-size: 140px;
    line-height: 1;
    margin: 0;
  }
  .dotted-rule {
    position: absolute;
    left: 84px;
    width: 716px;
    height: 0;
    border-top: 6px dotted var(--ink);
  }
  .dotted-rule.top { top: 398px; }
  .dotted-rule.bottom { top: 562px; }
  .event-date {
    position: absolute;
    left: 84px;
    top: 410px;
    width: 716px;
    text-align: center;
    font-family: "Oswald", sans-serif;
    font-weight: 500;
    font-size: 104px;
    line-height: 140px;
    margin: 0;
  }
  .venue-band {
    position: absolute;
    left: 90px;
    top: 594px;
    width: 715px;
    height: 104px;
    background: var(--silhouette);
    color: var(--accent);
    display: flex;
    align-items: center;
    justify-content: center;
    font-family: "Roboto Condensed", sans-serif;
    font-weight: 500;
    font-size: 60px;
    letter-spacing: 0.5px;
  }
</style>
</head>
<body>
  <main class="postcard">
    <div class="sunset-sky" role="img" aria-label="Glowing orange and red sunset sky with scattered clouds and light sparkles"></div>
    <div class="cross-on-hill" role="img" aria-label="Dark silhouette of a wooden cross standing on a hilltop"></div>

    <p class="host">Pell Ridge Camp and Retreat Lodge</p>
    <p class="presents">Presents</p>
    <h1 class="event-title">Mend Days</h1>

    <div class="dotted-rule top"></div>
    <p class="event-date">May 4 - 8 , 2015</p>
    <div class="dotted-rule bottom"></div>

    <div class="venue-band">PELL RIDGE CAMP</div>
  </main>
</body>
</html>
```